Presentation Folder for Brisk Estates

We are a new property management / real estate company in Denver Colorado and are in need of new stationary design. Attached are our business card and logo deigns. We are looking for our stationary design. We need a presentation folder design that is Professional, exciting, and approachable. We do not have a preference on folder layout (pockets, style of folding) but will most likely be using a standard two pocket folder design (roughly 9x12) but feel free to experiment with and folder style as long as we can find a place to print them. We would also like to have a matching letterhead/page design
Below is standard size of folder from lumo press
Full Bleed Size
20.87" x 16.68"
53 x 42.4 cm
6260 x 5004 pixels
Document Trim Size
20.75" x 16.56"
52.7 x 42.1 cm
6225 x 4969 pixels
Target Market(s)
We are attempting to target the top end of the real estate market in Denver Colorado. Are target market is investors in real estate.
Industry/Entity Type
Property Management
Font styles to use
Other font styles liked:
- Would like to keep font same to logo
Look and feel
Each slider illustrates characteristics of the customer's brand and the style your logo design should communicate.

```html
<!DOCTYPE html>
<html lang="en">
<head>
<meta charset="utf-8">
<title>Brisk Estates — Presentation Folder &amp; Letterhead</title>
<link href="https://fonts.googleapis.com/css2?family=Oswald:wght@500&family=Raleway:wght@400;500&display=swap" rel="stylesheet">
<style>
  :root{
    --stage:#5e5e5e;
    --stage-light:#8a8a8a;
    --brand:#5ab3d3;
    --brand-deep:#3f97b8;
    --brand-soft:#86c8e0;
    --paper:#ffffff;
    --ink:#4a4a4a;
    --caption:#ffffff;
    --ghost:rgba(255,255,255,.22);
    --ghost-blue:rgba(90,179,211,.12);
  }
  *{box-sizing:border-box;margin:0;padding:0}
  html,body{width:1200px;height:1000px;overflow:hidden}
  body{
    background:radial-gradient(ellipse at 30% 20%,var(--stage-light),var(--stage) 70%);
    font-family:"Raleway",sans-serif;color:var(--ink);position:relative;
  }
  .piece{position:absolute;box-shadow:0 6px 18px rgba(0,0,0,.35)}
  .caption{position:absolute;color:var(--caption);font-size:15px;font-family:"Raleway",sans-serif}

  /* lockup */
  .lockup{display:flex;align-items:center;gap:6px}
  .lockup-dot{border-radius:50%;background:var(--brand);flex:none}
  .lockup-name{font-family:"Oswald",sans-serif;font-weight:500;text-transform:uppercase;color:var(--brand);line-height:1;letter-spacing:.3px}
  .lockup-tag{font-family:"Raleway",sans-serif;color:var(--ink);line-height:1.2}
  .lockup.on-blue .lockup-dot{background:var(--paper)}
  .lockup.on-blue .lockup-name,.lockup.on-blue .lockup-tag{color:var(--paper)}

  .contact{list-style:none;font-size:5px;line-height:1.55;color:var(--ink)}
  .contact li::before{content:"";display:inline-block;width:3px;height:3px;background:var(--brand);margin-right:3px;vertical-align:middle}

  .ghost-ring{position:absolute;border-radius:50%}

  /* folder outside */
  .folder-outside{left:20px;top:20px;width:540px;height:410px;display:flex}
  .folder-back{position:relative;width:270px;height:100%;background:var(--brand);overflow:hidden}
  .folder-back .ghost-ring{left:20px;top:70px;width:240px;height:240px;border:20px solid var(--ghost)}
  .folder-back-footer{position:absolute;left:0;bottom:0;width:100%;height:62px;background:var(--paper);display:flex;align-items:center;justify-content:space-between;padding:0 16px}
  .folder-front{position:relative;width:270px;height:100%;background:var(--paper);overflow:hidden}
  .folder-front .ghost-ring{left:40px;top:-170px;width:300px;height:300px;border:16px solid var(--brand)}
  .folder-front .lockup{position:absolute;right:16px;bottom:60px}

  /* folder inside */
  .folder-inside{left:600px;top:20px;width:560px;height:410px;display:flex}
  .inside-left{position:relative;width:280px;height:100%;background:var(--brand);overflow:hidden}
  .inside-left .ghost-ring{left:20px;top:80px;width:250px;height:250px;border:20px solid var(--ghost)}
  .inside-right{position:relative;width:280px;height:100%;background:var(--brand-deep);overflow:hidden;border-left:1px solid rgba(0,0,0,.08)}
  .inside-right .ghost-ring{left:40px;top:-60px;width:240px;height:240px;border:18px solid var(--ghost)}
  .pocket{position:absolute;left:0;bottom:0;width:100%;height:150px}
  .pocket svg{display:block}
  .pocket .lockup{position:absolute;left:50%;top:72px;transform:translateX(-50%)}

  /* letterheads */
  .sheet{top:520px;width:260px;height:336px;background:var(--paper);overflow:hidden}
  .sheet .lockup{position:absolute;left:16px;top:18px}
  .sheet .contact{position:absolute;right:16px;top:16px}
  .sheet-one{left:50px}
  .sheet-one .ghost-ring{left:10px;top:230px;width:240px;height:240px;border:18px solid var(--ghost-blue)}
  .sheet-one-foot{position:absolute;left:0;bottom:0;width:100%;height:8px;background:var(--brand)}
  .sheet-two{left:460px}
  .sheet-two .ghost-ring{right:-20px;bottom:-10px;width:90px;height:90px;border:8px solid var(--ghost-blue)}
  .sheet-two .contact{top:auto;right:auto;left:16px;bottom:24px}
  .sheet-two-foot{position:absolute;left:0;bottom:0;width:100%;height:10px;background:var(--brand)}
  .sheet-back{left:870px;background:var(--brand)}
  .sheet-back .ghost-ring{left:10px;top:-40px;width:240px;height:240px;border:18px solid var(--ghost)}
  .sheet-back .lockup{left:50%;top:210px;transform:translateX(-50%)}
</style>
</head>
<body>

<!-- Folder outside spread -->
<section class="piece folder-outside" aria-label="Folder cover">
  <div class="folder-back">
    <div class="ghost-ring"></div>
    <footer class="folder-back-footer">
      <div class="lockup">
        <div>
          <div class="lockup-name" style="font-size:15px">Brisk Estates</div>
          <div class="lockup-tag" style="font-size:5px">Property Management and Real Estate</div>
        </div>
      </div>
      <ul class="contact">
        <li>(303) 555-0147</li>
        <li>(720) 555-0162</li>
        <li>info@briskestatesco.com</li>
        <li>P.O. Box 1042, Denver, CO 80201</li>
      </ul>
    </footer>
  </div>
  <div class="folder-front">
    <div class="ghost-ring"></div>
    <div class="lockup">
      <span class="lockup-dot" style="width:18px;height:18px"></span>
      <div>
        <div class="lockup-name" style="font-size:17px">Brisk Estates</div>
        <div class="lockup-tag" style="font-size:6px">Property Management and Real Estate</div>
      </div>
    </div>
  </div>
</section>
<p class="caption" style="left:240px;top:442px">Folder cover</p>

<!-- Folder inside spread -->
<section class="piece folder-inside" aria-label="Folder inside">
  <div class="inside-left"><div class="ghost-ring"></div></div>
  <div class="inside-right">
    <div class="ghost-ring"></div>
    <div class="pocket">
      <svg width="280" height="150" viewBox="0 0 280 150" aria-hidden="true">
        <path d="M0 20 Q140 0 280 40 L280 150 L0 150 Z" fill="#6cbcd9"/>
        <path d="M0 20 Q140 0 280 40" fill="none" stroke="#2f84a5" stroke-width="3"/>
      </svg>
      <div class="lockup on-blue">
        <span class="lockup-dot" style="width:14px;height:14px"></span>
        <div>
          <div class="lockup-name" style="font-size:13px">Brisk Estates</div>
          <div class="lockup-tag" style="font-size:5px">Property Management and Real Estate</div>
        </div>
      </div>
    </div>
  </div>
</section>
<p class="caption" style="left:840px;top:442px">Folder inside</p>

<!-- Letterhead option 1 -->
<section class="piece sheet sheet-one" aria-label="Letterhead front option 1">
  <div class="ghost-ring"></div>
  <div class="lockup">
    <span class="lockup-dot" style="width:12px;height:12px"></span>
    <div>
      <div class="lockup-name" style="font-size:12px">Brisk Estates</div>
      <div class="lockup-tag" style="font-size:4.5px">Property Management and Real Estate</div>
    </div>
  </div>
  <ul class="contact">
    <li>(303) 555-0147</li>
    <li>(720) 555-0162</li>
    <li>(720) 555-0188</li>
    <li>info@briskestatesco.com</li>
  </ul>
  <div class="sheet-one-foot"></div>
</section>
<p class="caption" style="left:110px;top:872px">Letterhead_front_option 1</p>

<!-- Letterhead option 2 -->
<section class="piece sheet sheet-two" aria-label="Letterhead front option 2">
  <div class="ghost-ring"></div>
  <div class="lockup">
    <span class="lockup-dot" style="width:12px;height:12px"></span>
    <div>
      <div class="lockup-name" style="font-size:12px">Brisk Estates</div>
      <div class="lockup-tag" style="font-size:4.5px">Property Management and Real Estate</div>
    </div>
  </div>
  <ul class="contact">
    <li>(303) 555-0147</li>
    <li>(720) 555-0162</li>
    <li>(720) 555-0188</li>
    <li>info@briskestatesco.com</li>
    <li>P.O. Box 1042, Denver, CO 80201</li>
  </ul>
  <div class="sheet-two-foot"></div>
</section>
<p class="caption" style="left:515px;top:872px">Letterhead_front_option 2</p>

<!-- Letterhead back -->
<section class="piece sheet sheet-back" aria-label="Letterhead back">
  <div class="ghost-ring"></div>
  <div class="lockup on-blue">
    <span class="lockup-dot" style="width:22px;height:22px"></span>
    <div>
      <div class="lockup-name" style="font-size:22px">Brisk Estates</div>
      <div class="lockup-tag" style="font-size:7px">Property Management and Real Estate</div>
    </div>
  </div>
</section>
<p class="caption" style="left:955px;top:872px">Letterhead_back</p>

</body>
</html>
```